A modern, fresh introduction to Buddhism

I need a book cover for an A6 sized book to be used both for ebook and hard copy. The author is a young, modern Buddhist teacher of high standing who has written this short intro to Buddhism in an informal Q & As format using modern, accessible language to convey profound and meaningful ideas to the general public. The author is Tibetan, but teaches worldwide and is very personable and dynamic. The cover should portray this and have a fresh yet authentic feel to it (nothing new-agey!). Please see the author's websites www.norvalemtasheteacher.org and www.pwrt.org for reference, but do not feel that the design must align completely with the website designs.

Target Market(s)

General public both in Europe and America and in Asia ranging from teenagers to the elderly. A really broad audience.

Industry/Entity Type

Teacher

Requirements
Must have
• Please include the following text that on the front cover:

A Window onto Stillness

By Drawa Tsomen Lhundrup

Please include the following on the back cover:

Yunor Trenpa Publications (with attached logo above it)
Nice to have
• A simplistic, artistic, and modern look without any traditional religious images.
Should not have
• No buddha images or religious images. I would prefer a more simplistic, modern and artistic look.

```html
<!DOCTYPE html>
<html lang="en">
<head>
<meta charset="utf-8">
<title>A Window onto Stillness — Book Cover</title>
<link href="https://fonts.googleapis.com/css2?family=Roboto+Condensed:wght@300;400;700&display=swap" rel="stylesheet">
<style>
  :root {
    --backdrop: #4f8f96;
    --backdrop-light: #7fb8bd;
    --paper: #f7f3ec;
    --ink-red: #b0102e;
    --ink-crimson: #8e0a24;
    --ink-orange: #d9731c;
    --ink-gold: #e2a81e;
    --ink-yellow: #f0c43a;
    --band-red: #c8102e;
    --type-white: #ffffff;
  }
  * { margin: 0; padding: 0; box-sizing: border-box; }
  html, body {
    width: 1200px;
    height: 900px;
    overflow: hidden;
  }
  body {
    background: radial-gradient(ellipse at 50% 40%, var(--backdrop-light) 0%, var(--backdrop) 70%);
    font-family: "Roboto Condensed", "Arial Narrow", sans-serif;
  }
  .cover {
    position: absolute;
    left: 300px;
    top: 30px;
    width: 600px;
    height: 840px;
    overflow: hidden;
    background: var(--paper);
  }
  .cover-art {
    position: absolute;
    inset: 0;
    background:
      radial-gradient(ellipse 34% 22% at 78% 40%, var(--ink-red) 0%, rgba(176,16,46,0.85) 45%, rgba(176,16,46,0) 100%),
      radial-gradient(ellipse 30% 20% at 35% 10%, var(--ink-crimson) 0%, rgba(142,10,36,0.7) 50%, rgba(142,10,36,0) 100%),
      radial-gradient(ellipse 25% 18% at 20% 45%, rgba(176,16,46,0.75) 0%, rgba(176,16,46,0) 100%),
      radial-gradient(ellipse 30% 25% at 88% 10%, var(--paper) 0%, rgba(247,243,236,0.9) 50%, rgba(247,243,236,0) 100%),
      radial-gradient(ellipse 22% 20% at 90% 70%, rgba(247,243,236,0.9) 0%, rgba(247,243,236,0) 100%),
      radial-gradient(ellipse 40% 30% at 35% 65%, var(--ink-orange) 0%, rgba(217,115,28,0) 100%),
      linear-gradient(180deg, var(--ink-gold) 0%, var(--ink-orange) 35%, var(--ink-gold) 65%, var(--ink-yellow) 100%);
  }
  .cover-type {
    position: absolute;
    left: 90px;
    top: 190px;
    right: 30px;
    color: var(--type-white);
  }
  .title-lead {
    font-weight: 400;
    font-size: 60px;
    line-height: 1;
    letter-spacing: 1px;
    text-transform: uppercase;
  }
  .title-main {
    font-weight: 400;
    font-size: 118px;
    line-height: 1;
    letter-spacing: -1px;
    margin-top: 6px;
  }
  .subtitle-band {
    display: inline-block;
    margin-top: 12px;
    margin-left: -4px;
    padding: 4px 12px 5px;
    background: var(--band-red);
    font-weight: 700;
    font-size: 19px;
    letter-spacing: 0.3px;
    text-transform: uppercase;
  }
  .byline {
    margin-top: 24px;
    font-weight: 400;
    font-size: 26px;
    line-height: 1;
  }
  .author {
    margin-top: 10px;
    font-weight: 700;
    font-size: 30px;
    line-height: 1;
  }
</style>
</head>
<body>
  <main class="cover">
    <div class="cover-art" role="img" aria-label="Abstract swirling clouds of red and golden-yellow ink spreading through water on a pale ground"></div>
    <div class="cover-type">
      <h1>
        <span class="title-lead">A Window onto</span><br>
        <span class="title-main">Stillness</span>
      </h1>
      <p class="subtitle-band">A Short Introduction to the Buddha’s Teaching</p>
      <p class="byline">BY</p>
      <p class="author">Drawa Tsomen Lhundrup</p>
    </div>
  </main>
</body>
</html>
```